Box Truck wrap for an insulation company

Full wrap design for a box truck.
The services we offer are

Target Market(s)

Homeowners

Industry/Entity Type

Home Improvement

Colors
acd136
0455a3

Requirements
Must have
• Lic# 3859160 (Small. Required by law)
559-318-2264 (large)
Www.Marlowheatworks.com
Logo (large)
We fix high utility bills

Insulation
Whole house fans
Insulation removal
Window film
Thermal imaging inspections
Solar
and more
Nice to have
• a blended collage of solar, insulation, and thermal imaging

```html
<!DOCTYPE html>
<html lang="en">
<head>
<meta charset="utf-8">
<title>Marlow Heatworks – Box Truck Wrap</title>
<link href="https://fonts.googleapis.com/css2?family=Dosis:wght@600;700;800&family=Oswald:wght@500&display=swap" rel="stylesheet">
<style>
  :root {
    --green: #5ba33b;
    --green-deep: #3f8a2c;
    --lime: #acd136;
    --lime-text: #c8e04a;
    --navy: #0455a3;
    --navy-dark: #1d3d7c;
    --cab-navy: #1b3f86;
    --pill: #1f5a2a;
    --white: #ffffff;
    --ink: #111111;
    --rule: #c9c9c9;
  }
  * { margin: 0; padding: 0; box-sizing: border-box; }
  html, body { width: 1167px; height: 1200px; overflow: hidden; background: var(--white); }
  .canvas { position: relative; width: 1167px; height: 1200px; }
  .option-label {
    position: absolute; left: 906px;
    font-family: "Oswald", sans-serif; font-weight: 500; font-size: 32px;
    color: var(--ink); letter-spacing: 0.5px; line-height: 1;
  }
  .divider { position: absolute; left: 0; top: 588px; width: 1167px; height: 4px; background: var(--rule); }

  .box-panel {
    position: absolute; width: 880px; height: 459px; overflow: hidden;
    transform: scale(0.68); transform-origin: 0 0;
  }
  .box-panel svg.art { position: absolute; inset: 0; }
  .brand-name {
    position: absolute; left: 20px; top: 62px; width: 500px;
    font-family: "Dosis", sans-serif; font-weight: 700; font-size: 40px;
    color: var(--white); letter-spacing: 3px; text-align: center; line-height: 1; white-space: nowrap;
  }
  .brand-rule { position: absolute; left: 70px; top: 118px; width: 400px; height: 2px; background: var(--white); }
  .headline {
    position: absolute; left: 20px; top: 172px; width: 500px; text-align: center; white-space: nowrap;
    font-family: "Dosis", sans-serif; font-weight: 800; font-size: 33px; line-height: 1; color: var(--lime-text);
  }
  .services {
    position: absolute; left: 20px; top: 218px; width: 500px; text-align: center; white-space: nowrap;
    font-family: "Dosis", sans-serif; font-weight: 800; font-size: 25px; line-height: 28px;
    color: var(--white); text-transform: uppercase;
  }
  .services small { font-size: 16px; }
  .phone-pill {
    position: absolute; left: 135px; top: 343px; width: 270px; height: 46px;
    border-radius: 23px; background: var(--pill);
    font-family: "Dosis", sans-serif; font-weight: 800; font-size: 31px; line-height: 46px;
    color: var(--white); text-align: center;
  }
  .web-address {
    position: absolute; left: 20px; top: 402px; width: 500px; text-align: center;
    font-family: "Dosis", sans-serif; font-weight: 700; font-size: 16px; color: var(--white);
    text-transform: uppercase; letter-spacing: 0.5px;
  }
  .license {
    position: absolute; top: 398px;
    font-family: "Dosis", sans-serif; font-weight: 700; font-size: 11px; color: var(--ink); white-space: nowrap;
  }
  .rating-badge { position: absolute; width: 52px; height: 34px; background: var(--navy-dark); border: 1px solid var(--white); }

  .cab-panel { position: absolute; width: 332px; height: 272px; }
</style>
</head>
<body>
<div class="canvas">

  <!-- Option 2 -->
  <div class="option-label" style="top:168px">OPTION 2</div>
  <section class="box-panel" style="left:118px; top:148px">
    <svg class="art" viewBox="0 0 880 459" width="880" height="459">
      <defs>
        <linearGradient id="boxGreen" x1="0" y1="0" x2="1" y2="0">
          <stop offset="0" stop-color="#4f9a33"/><stop offset="1" stop-color="#6cb33f"/>
        </linearGradient>
        <linearGradient id="collageTones" x1="0" y1="0" x2="0" y2="1">
          <stop offset="0" stop-color="#d9d4cd"/><stop offset="0.45" stop-color="#b98a55"/><stop offset="1" stop-color="#c7a0b4"/>
        </linearGradient>
        <linearGradient id="solarTones" x1="0" y1="0" x2="0" y2="1">
          <stop offset="0" stop-color="#d6e0ea"/><stop offset="1" stop-color="#3f5e9a"/>
        </linearGradient>
      </defs>
      <rect width="880" height="459" fill="url(#boxGreen)"/>
      <rect x="0" y="0" width="30" height="459" fill="var(--green-deep)"/>
      <path d="M450 0 C560 120 560 340 520 459 L880 459 L880 0 Z" fill="var(--lime)"/>
      <path d="M470 0 C575 120 575 340 540 459 L880 459 L880 0 Z" fill="var(--white)"/>
      <path d="M510 0 C600 120 600 340 565 459 L880 459 L880 0 Z" fill="url(#collageTones)" role="img" aria-label="Collage of a house, thermal imaging camera and blown insulation"/>
      <path d="M770 0 C745 170 710 310 650 459 L880 459 L880 0 Z" fill="var(--navy-dark)"/>
      <path d="M785 0 C762 170 728 310 670 459 L880 459 L880 0 Z" fill="url(#solarTones)" role="img" aria-label="Photo of workers installing solar panels on a roof"/>
      <path d="M800 400 L880 330 L880 360 L820 459 L785 459 Z" fill="var(--lime)"/>
    </svg>
    <div class="brand-name">MARLOW HEATWORKS</div>
    <div class="brand-rule"></div>
    <div class="headline">WE FIX HIGH UTILITY BILLS</div>
    <div class="services">Insulation • Window Film<br>Whole House Fans • Solar<br>Thermal Imaging Inspections<br>Insulation Removal <small>and</small> More!</div>
    <div class="phone-pill">559-318-2264</div>
    <div class="web-address">www.marlowheatworks.com</div>
    <div class="license" style="left:590px">LIC# 3859160</div>
    <div class="rating-badge" style="left:670px; top:372px"></div>
  </section>
  <svg class="cab-panel" style="left:728px; top:256px" viewBox="0 0 332 272" width="332" height="272">
    <path d="M0 0 L110 0 C160 20 200 70 230 115 L300 170 C325 185 332 205 332 230 L332 272 L0 272 Z" fill="var(--cab-navy)"/>
    <path d="M95 0 L118 0 C70 60 40 160 30 272 L8 272 C18 160 48 60 95 0 Z" fill="var(--lime)"/>
    <path d="M75 0 L95 0 C48 60 18 160 8 272 L0 272 L0 230 C10 140 35 60 75 0 Z" fill="var(--white)"/>
  </svg>

  <div class="divider"></div>

  <!-- Option 3 -->
  <div class="option-label" style="top:748px">OPTION 3</div>
  <section class="box-panel" style="left:126px; top:716px">
    <svg class="art" viewBox="0 0 880 459" width="880" height="459">
      <rect width="880" height="459" fill="url(#boxGreen)"/>
      <rect x="0" y="0" width="30" height="459" fill="var(--green-deep)"/>
      <path d="M450 0 C560 120 560 340 520 459 L880 459 L880 0 Z" fill="var(--lime)"/>
      <path d="M470 0 C575 120 575 340 540 459 L880 459 L880 0 Z" fill="var(--white)"/>
      <path d="M510 0 C600 120 600 340 565 459 L880 459 L880 0 Z" fill="url(#collageTones)" role="img" aria-label="Collage of a house, thermal imaging camera and blown insulation"/>
      <path d="M770 0 C745 170 710 310 650 459 L880 459 L880 0 Z" fill="var(--navy-dark)"/>
      <path d="M785 0 C762 170 728 310 670 459 L880 459 L880 0 Z" fill="url(#solarTones)" role="img" aria-label="Photo of workers installing solar panels on a roof"/>
      <path d="M800 400 L880 330 L880 360 L820 459 L785 459 Z" fill="var(--lime)"/>
      <rect x="480" y="232" width="175" height="227" rx="30" fill="#7fbf3f" role="img" aria-label="Cartoon house mascot giving a thumbs up"/>
    </svg>
    <div class="brand-name">MARLOW HEATWORKS</div>
    <div class="brand-rule"></div>
    <div class="headline">WE FIX HIGH UTILITY BILLS</div>
    <div class="services">Insulation • Window Film<br>Whole House Fans • Solar<br>Thermal Imaging Inspections<br>Insulation Removal <small>and</small> More!</div>
    <div class="phone-pill">559-318-2264</div>
    <div class="web-address">www.marlowheatworks.com</div>
    <div class="rating-badge" style="left:668px; top:378px"></div>
    <div class="license" style="left:738px">LIC# 3859160</div>
  </section>
  <svg class="cab-panel" style="left:732px; top:824px" viewBox="0 0 332 272" width="332" height="272">
    <path d="M0 0 L110 0 C160 20 200 70 230 115 L300 170 C325 185 332 205 332 230 L332 272 L0 272 Z" fill="var(--cab-navy)"/>
    <path d="M95 0 L118 0 C70 60 40 160 30 272 L8 272 C18 160 48 60 95 0 Z" fill="var(--lime)"/>
    <path d="M75 0 L95 0 C48 60 18 160 8 272 L0 272 L0 230 C10 140 35 60 75 0 Z" fill="var(--white)"/>
  </svg>

</div>
</body>
</html>
```